Website Redesign - Money is Guaranteed!

I would like a site similar to this: http://www.givewheelsforheroes.example

old site: http://www.autosforpatriots.example

Create a professional website; a car donation site seeking leads to return calls.

Please see http://www.givewheelsforheroes.example for the concept I am after.

The webpage should have a professional feel. The pages to include are 'Home', 'About us' and 'Get Started'

Industry/Entity Type

It Professional

Coding

Coded - Design and coding required

Number of Pages Required

1 page

```html
<!DOCTYPE html>
<html lang="en">
<head>
<meta charset="utf-8">
<title>Autos for Patriots – Donate Your Car</title>
<link rel="stylesheet" href="https://fonts.googleapis.com/css2?family=Open+Sans:wght@400;600;700;800&display=swap">
<style>
:root{
  --navy:#0d2a7a;
  --navy-dark:#061a55;
  --red:#a5120f;
  --red-dark:#7e0b09;
  --gold:#c9a24a;
  --white:#ffffff;
  --ink:#2b2b2b;
  --muted:#555555;
  --page:#e9e9e9;
  --line:#cfcfcf;
  --field:#ffffff;
}
*{box-sizing:border-box;margin:0;padding:0}
html,body{width:1200px;height:2344px;overflow:hidden}
body{background:var(--page);font-family:"Open Sans",Arial,sans-serif;color:var(--ink);position:relative}
.abs{position:absolute}
.site{position:absolute;left:14px;top:14px;width:1172px;height:2314px;background:var(--white);overflow:hidden}

/* header */
.header{left:0;top:0;width:1172px;height:153px;background:linear-gradient(100deg,var(--navy-dark),var(--navy) 45%,#1d3d96 70%,var(--navy-dark))}
.brand{display:flex;align-items:center;gap:12px;font-weight:800;font-size:30px;color:var(--white);letter-spacing:.5px}
.brand-mark{width:26px;height:26px;background:var(--red);border-radius:4px}
.header .brand{left:44px;top:56px}
.call-box{left:775px;top:0;width:350px;height:153px;background:var(--red)}
.call-box svg{position:absolute;left:22px;top:44px}
.call-label{left:99px;top:42px;font-size:18px;font-weight:700;color:var(--white)}
.call-number{left:99px;top:62px;font-size:30px;font-weight:800;color:var(--white);letter-spacing:.3px}
.call-note{left:99px;top:102px;font-size:12.5px;font-weight:700;color:var(--white)}

.nav{left:0;top:153px;width:1172px;height:45px;background:var(--red);display:flex;align-items:center}
.nav a{position:absolute;color:var(--white);text-decoration:none;font-size:15px;font-weight:700;top:12px}

/* hero */
.hero-photo{left:0;top:198px;width:775px;height:386px;background:linear-gradient(160deg,#7a6a55 0%,#d9b37a 35%,#f3d9a4 55%,#8a7458 80%,#3c3128 100%)}
.form-tab{left:763px;top:153px;width:376px;height:50px;background:var(--white);display:flex;align-items:center;justify-content:center;font-size:18px;font-weight:800;color:var(--navy);box-shadow:0 3px 6px rgba(0,0,0,.25)}
.form-panel{left:775px;top:203px;width:350px;height:381px;background:var(--navy)}
.form-title{left:0;top:27px;width:350px;text-align:center;font-size:16px;font-weight:700;color:var(--white)}
.field{position:absolute;height:30px;background:var(--field);border-radius:3px;font-size:11.5px;font-weight:600;color:#333;padding:7px 8px}
.field.select::after{content:"";position:absolute;right:8px;top:11px;border:6px solid transparent;border-top:7px solid #555}
.field.select::before{content:"";position:absolute;right:26px;top:4px;bottom:4px;border-left:1px solid #bbb}
.btn-donate{left:19px;top:314px;width:152px;height:39px;background:var(--red);border-radius:3px;color:var(--white);font-size:14px;font-weight:700;display:flex;align-items:center;justify-content:center}

/* banner */
.banner{left:0;top:567px;width:1172px;height:245px;background:linear-gradient(180deg,#d9d9d9,#ececec 60%,#f2f2f2)}
.banner-shape{left:0;top:567px}
.banner-text{left:58px;top:628px;color:var(--white);font-weight:800}
.banner-text .l1{font-size:27px;line-height:34px}
.banner-text .l2{font-size:51px;line-height:58px;color:var(--gold);letter-spacing:1px}
.banner-text .l3{font-size:28px;line-height:36px}
.benefit{position:absolute;top:640px;width:120px;text-align:center}
.benefit svg{display:block;margin:0 auto 10px}
.benefit p{font-size:12.5px;line-height:16px;font-weight:700;color:var(--red)}
.car-photo{left:816px;top:744px;width:360px;height:180px;border-radius:60px 90px 20px 20px;background:linear-gradient(180deg,#d33a30,#9e1712 60%,#333 100%)}

/* how to */
.section-title{position:absolute;left:0;width:1172px;text-align:center;font-size:28px;font-weight:800;color:var(--navy)}
.section-title span{color:var(--red)}
.section-title::before,.section-title::after{content:"";display:inline-block;width:94px;height:1px;background:var(--line);vertical-align:middle;margin:0 22px}
.step{position:absolute;top:940px}
.step h3{position:absolute;font-size:14.5px;line-height:19px;font-weight:800;color:var(--navy);width:260px}
.step p{position:absolute;font-size:13px;line-height:18px;color:#333;font-weight:600;width:235px}

/* why */
.why{left:0;top:1142px;width:1172px;height:421px;background:linear-gradient(180deg,#e4e6ec,#f0f0f2 50%,#e6e7eb)}
.why-list{left:136px;top:1281px;list-style:none}
.why-list li{position:relative;height:32px;padding-left:28px;font-size:13.5px;line-height:24px;color:#333}
.why-list li b{font-weight:700}
.why-list li::before{content:"";position:absolute;left:0;top:2px;width:20px;height:20px;border-radius:50%;background:var(--red)}
.why-list li::after{content:"";position:absolute;left:5px;top:9px;width:6px;height:6px;border-top:2px solid #fff;border-right:2px solid #fff;transform:rotate(45deg)}

/* faq */
.faq-item{position:absolute;left:78px;width:475px;height:37px;border:1px solid var(--line);border-radius:12px;background:var(--white);padding:7px 16px;font-size:14px;font-weight:700;color:#222}
.faq-item::after{content:"";position:absolute;right:17px;top:11px;width:7px;height:7px;border-right:2px solid #333;border-bottom:2px solid #333;transform:rotate(45deg)}
.faq-item.open{height:133px}
.faq-item.open::after{top:15px;transform:rotate(-135deg)}
.faq-item.open p{font-size:12.5px;line-height:19px;font-weight:400;color:#333;margin-top:6px}
.faq-photo{left:586px;top:1678px;width:522px;height:416px;background:linear-gradient(160deg,#b3272c 0%,#e9e3e0 25%,#1b3b8c 45%,#8f8f82 70%,#6b6a55 100%)}

/* footer */
.footer{left:0;top:2150px;width:1172px;height:143px;background:linear-gradient(100deg,var(--navy-dark),var(--navy) 50%,var(--navy-dark))}
.footer .brand{left:0;width:1172px;justify-content:center;top:53px}
.legal{left:0;top:2278px;width:1172px;height:36px;background:var(--red);color:var(--white);font-size:11px;font-weight:700;display:flex;align-items:center;justify-content:center}
</style>
</head>
<body>
<div class="site">

  <header class="header abs">
    <div class="brand abs"><span class="brand-mark"></span>AUTOS FOR PATRIOTS</div>
    <div class="call-box abs">
      <svg width="64" height="64" viewBox="0 0 64 64" aria-hidden="true">
        <circle cx="32" cy="32" r="29" fill="none" stroke="#fff" stroke-width="3.5"/>
        <path d="M22 17c2-1 4 0 5 2l3 6c1 2 0 3-1 4l-2 2c1 4 5 8 9 9l2-2c1-1 3-2 4-1l6 3c2 1 3 3 2 5l-2 3c-2 2-5 3-8 2-10-3-18-11-21-21-1-3 0-6 2-8z" fill="#fff"/>
      </svg>
      <div class="call-label abs">CALL TODAY TO DONATE</div>
      <div class="call-number abs">1-800-555-0147</div>
      <div class="call-note abs">Live Operators Available - 7 Days A Week</div>
    </div>
  </header>

  <nav class="nav abs">
    <a style="left:172px">HOW TO DONATE</a>
    <a style="left:356px">WHY DONATE</a>
    <a style="left:512px">FAQ</a>
    <a style="left:595px">ABOUT</a>
  </nav>

  <div class="hero-photo abs" role="img" aria-label="Silhouetted soldiers raising an American flag against a sunset sky"></div>

  <section class="form-panel abs">
    <div class="form-title abs">Full Tax Deduction - Running or Not</div>
    <div class="field" style="left:19px;top:50px;width:153px">First Name</div>
    <div class="field" style="left:180px;top:50px;width:153px">Last Name</div>
    <div class="field" style="left:19px;top:86px;width:153px">Daytime Phone</div>
    <div class="field" style="left:180px;top:86px;width:153px">Email</div>
    <div class="field" style="left:19px;top:124px;width:314px">Pickup Address</div>
    <div class="field" style="left:19px;top:161px;width:314px">Pickup City</div>
    <div class="field select" style="left:19px;top:197px;width:153px">Pickup State</div>
    <div class="field" style="left:180px;top:197px;width:153px">Zip Code</div>
    <div class="field select" style="left:19px;top:235px;width:153px">Choose Year</div>
    <div class="field select" style="left:180px;top:235px;width:153px">Choose Make</div>
    <div class="field" style="left:19px;top:272px;width:314px">Vehicle Model</div>
    <div class="btn-donate abs">DONATE NOW</div>
  </section>
  <div class="form-tab abs">DONATE YOUR CAR ONLINE</div>

  <div class="banner abs"></div>
  <svg class="banner-shape abs" width="540" height="245" viewBox="0 0 540 245" aria-hidden="true">
    <defs><linearGradient id="bannerBlue" x1="0" x2="1"><stop offset="0" stop-color="#0a2470"/><stop offset="1" stop-color="#1e46a8"/></linearGradient></defs>
    <polygon points="0,0 424,0 540,225 0,225" fill="url(#bannerBlue)"/>
    <polygon points="0,225 540,225 530,245 0,245" fill="#0a1a4c"/>
  </svg>
  <div class="banner-text abs">
    <div class="l1">DONATE YOUR CAR TO</div>
    <div class="l2">VETERANS</div>
    <div class="l3">MAKE A DIFFERENCE</div>
  </div>

  <div class="benefit" style="left:507px">
    <svg width="60" height="60" viewBox="0 0 60 60" aria-hidden="true"><path d="M48 16A25 25 0 1 0 54 30" fill="none" stroke="#0d2a7a" stroke-width="4"/><path d="M18 30l9 9 24-26" fill="none" stroke="#0d2a7a" stroke-width="5"/></svg>
    <p>You have<br>no costs</p>
  </div>
  <div class="benefit" style="left:637px">
    <svg width="60" height="60" viewBox="0 0 60 60" aria-hidden="true"><rect x="28" y="22" width="26" height="20" rx="3" fill="#0d2a7a"/><path d="M6 42h24V28H16z" fill="#0d2a7a"/><path d="M18 6l10 16" stroke="#0d2a7a" stroke-width="3"/><circle cx="14" cy="46" r="6" fill="#a5120f"/><circle cx="44" cy="46" r="6" fill="#a5120f"/></svg>
    <p>Free towing,<br>running or not</p>
  </div>
  <div class="benefit" style="left:757px">
    <svg width="60" height="60" viewBox="0 0 60 60" aria-hidden="true"><path d="M14 4h32v52l-5-4-5 4-6-4-6 4-5-4-5 4z" fill="none" stroke="#0d2a7a" stroke-width="3"/><path d="M20 14h20M20 20h20M20 40h20" stroke="#0d2a7a" stroke-width="2.5"/><text x="30" y="35" text-anchor="middle" font-size="12" font-weight="800" fill="#a5120f" font-family="Open Sans, sans-serif">$</text></svg>
    <p>We issue you an<br>IRS tax receipt</p>
  </div>
  <div class="benefit" style="left:896px">
    <svg width="60" height="60" viewBox="0 0 60 60" aria-hidden="true"><rect x="14" y="6" width="34" height="44" rx="2" fill="none" stroke="#0d2a7a" stroke-width="3"/><circle cx="27" cy="28" r="11" fill="#fff" stroke="#0d2a7a" stroke-width="3"/><path d="M35 36l12 14" stroke="#0d2a7a" stroke-width="5"/><path d="M27 21v8M27 32v2" stroke="#a5120f" stroke-width="3"/></svg>
    <p>We take care of<br>all paperwork.</p>
  </div>
  <div class="benefit" style="left:1023px">
    <svg width="60" height="60" viewBox="0 0 60 60" aria-hidden="true"><rect x="12" y="8" width="36" height="46" rx="3" fill="none" stroke="#0d2a7a" stroke-width="3"/><rect x="22" y="4" width="16" height="8" rx="2" fill="#0d2a7a"/><rect x="20" y="24" width="20" height="10" rx="3" fill="#0d2a7a"/><path d="M20 42h20M20 47h20" stroke="#0d2a7a" stroke-width="2.5"/></svg>
    <p>We take care of<br>DMV &amp; Smog issues</p>
  </div>

  <div class="car-photo abs" role="img" aria-label="Red classic muscle car with white racing stripes"></div>

  <h2 class="section-title" style="top:878px">HOW TO <span>DONATE</span></h2>

  <div class="step" style="left:58px">
    <svg class="abs" style="left:0;top:0" width="80" height="90" viewBox="0 0 80 90" aria-hidden="true"><rect x="14" y="0" width="62" height="10" fill="#a5120f"/><rect x="28" y="18" width="48" height="10" fill="#a5120f"/><rect x="14" y="36" width="62" height="10" fill="#a5120f"/><path d="M4 90l22-26-8-6 26-6-6 26-6-8-22 26z" fill="#a5120f"/></svg>
    <h3 style="left:100px;top:53px">CALL US AT 1-800-555-0147 OR<br>FILL OUT THE ONLINE FORM</h3>
    <p style="left:100px;top:101px">Donating your vehicle is easy and donation is accepted nationwide.</p>
  </div>
  <div class="step" style="left:436px">
    <svg class="abs" style="left:0;top:20px" width="96" height="70" viewBox="0 0 96 70" aria-hidden="true"><path d="M4 48V26l14-12h22v34z" fill="#a5120f"/><rect x="42" y="30" width="34" height="18" fill="#a5120f"/><path d="M40 20L86 4" stroke="#a5120f" stroke-width="4"/><path d="M86 4v22" stroke="#a5120f" stroke-width="3"/><circle cx="18" cy="54" r="8" fill="#fff" stroke="#a5120f" stroke-width="4"/><circle cx="62" cy="54" r="8" fill="#fff" stroke="#a5120f" stroke-width="4"/></svg>
    <h3 style="left:110px;top:53px">WE TOW THE VEHICLE</h3>
    <p style="left:110px;top:83px">Any vehicles is accepted and we will arrange to pick up your vehicle when it is most convenient for you.</p>
  </div>
  <div class="step" style="left:826px">
    <svg class="abs" style="left:0;top:2px" width="70" height="92" viewBox="0 0 70 92" aria-hidden="true"><path d="M16 2h46v80H16z" fill="none" stroke="#a5120f" stroke-width="3"/><path d="M6 12h46v78H6z" fill="#fff" stroke="#a5120f" stroke-width="3"/><text x="29" y="40" text-anchor="middle" font-size="24" font-weight="800" fill="#a5120f" font-family="Open Sans, sans-serif">$</text><path d="M14 52h30v26H14zM14 60h30M14 69h30M24 52v26M34 52v26" fill="none" stroke="#a5120f" stroke-width="2"/></svg>
    <h3 style="left:108px;top:53px">TAX WRITE-OFF</h3>
    <p style="left:108px;top:83px">Once the vehicle donation is complete, you will receive your tax deductable vehicle donation receipt.</p>
  </div>

  <section class="why abs" role="img" aria-label="Faded background of soldiers saluting beneath a waving flag"></section>
  <h2 class="section-title" style="top:1213px">WHY DONATE <span>YOUR CAR TO US</span></h2>
  <ul class="why-list abs">
    <li><b>Top A+ Rated &amp; IRS 501(c)3 Approved :</b> Free 24/7 Pickup with No DMV Hassles.</li>
    <li><b>Free Local Towing :</b> We will pick up your car donation, running or not, when it's most convenient, at home or work.</li>
    <li><b>All Cars Accepted :</b> We take your car regardless of its condition or registration status.</li>
    <li><b>Income Tax Deduction :</b> We issue you an IRS tax receipt &amp; offer the largest resale network to get you the highest tax write-off possible.</li>
    <li><b>No Paperwork Hassles :</b> We take any car and handle everything: DMV, Smog and IRS paperwork.</li>
    <li><b>Car donations help fund programs :</b> And benefit National Patriot Services Trust. An IRS 501(c)3 nonprofit organization.</li>
    <li><b>Schedule a Free Pickup :</b> Complete the form and a representative will call you to arrange a convenient time to pickup your car.</li>
  </ul>

  <h2 class="section-title" style="top:1619px">FREQUENTLY ASKED <span>QUESTIONS</span></h2>
  <div class="faq-item" style="top:1678px">What types of vehicles can be donated?</div>
  <div class="faq-item open" style="top:1725px">What paperwork do I need to donate my vehicle?
    <p>All you need is a title, free of all liens. We will request some general information from you at the time of donation such as, the year, make, and model of the car, as well as its general mechanical condition. We accept all vehicles, running or non-running.</p>
  </div>
  <div class="faq-item" style="top:1866px">Is my donated vehicle tax -deductible?</div>
  <div class="faq-item" style="top:1913px">What if the vehicle is not registered in my name?</div>
  <div class="faq-item" style="top:1959px">How much will I receive as a tax deduction for my vehicle?</div>
  <div class="faq-item" style="top:2006px">When will I receive my tax receipt?</div>
  <div class="faq-item" style="top:2053px">How do I schedule a pick up?</div>
  <div class="faq-photo abs" role="img" aria-label="American flag blended over soldiers' boots marching on a road"></div>

  <footer class="footer abs">
    <div class="brand abs"><span class="brand-mark"></span>AUTOS FOR PATRIOTS</div>
  </footer>
  <div class="legal abs">COPYRIGHT © 2016 AUTOS FOR PATRIOTS. PRIVACY POLICY I TERMS &amp; CONDITIONS. ALL RIGHTS RESERVED.</div>

</div>
</body>
</html>
```